Business Card Design - Service Company

Use of the card mainly in living rooms and relations b2b We wish a card with a modern design, blue tones in the background would be a plus The card must be front / back (one side with the logo / the other with the information of contact )

Font styles to use
Serif

Requirements
Must have
• Using the map on the back of the business card Editable format! Photoshop CS2 / Illustrator CS2
Nice to have
• Maquis Vertex IT Pierre Blanche Commercial Center, 20480 Lorvanu 0495718243 Siret 71384096200018 APE 6203Y https://www.fb.com/ateliertech.maquisvertex www.maquis-vertex.com

```html
<!DOCTYPE html>
<html lang="fr">
<head>
<meta charset="utf-8">
<title>Maquis Vertex IT – Business Card</title>
<link rel="stylesheet" href="https://fonts.googleapis.com/css2?family=Montserrat:wght@400;500;600&display=swap">
<style>
  :root {
    --stage: #e9eaec;
    --brand-blue: #2b87c8;
    --ink-grey: #5b5c5e;
    --band-grey: #77787b;
    --paper: #ffffff;
  }
  * { box-sizing: border-box; margin: 0; padding: 0; }
  html, body { width: 1200px; height: 831px; overflow: hidden; }
  body {
    background: var(--stage);
    font-family: "Montserrat", sans-serif;
    display: flex;
    align-items: center;
    justify-content: center;
    gap: 40px;
  }
  .card {
    position: relative;
    width: 540px;
    height: 309px;
    border-radius: 4px;
    overflow: hidden;
    box-shadow: 0 6px 18px rgba(0,0,0,.18);
  }
  /* Front */
  .card--front {
    background: var(--brand-blue);
    display: flex;
    align-items: center;
    justify-content: center;
    gap: 12px;
  }
  .front-mark {
    width: 14px; height: 14px;
    background: var(--paper);
  }
  .front-name {
    color: var(--paper);
    font-size: 34px;
    font-weight: 600;
    letter-spacing: .5px;
  }
  /* Back */
  .card--back { background: var(--paper); color: var(--ink-grey); }
  .holder { position: absolute; left: 32px; top: 44px; }
  .holder-name { font-size: 22px; font-weight: 500; letter-spacing: 1px; }
  .holder-title { font-size: 11px; font-weight: 500; color: var(--brand-blue); margin-top: 2px; letter-spacing: .5px; }
  .divider {
    position: absolute; left: 32px; right: 30px; top: 98px;
    height: 2px; background: var(--brand-blue);
  }
  .brand {
    position: absolute; right: 30px; top: 52px;
    display: flex; align-items: center; gap: 8px;
  }
  .brand-name { font-size: 20px; font-weight: 600; color: var(--brand-blue); }
  .brand-mark { width: 10px; height: 10px; background: var(--brand-blue); }
  .contacts { position: absolute; left: 32px; top: 116px; list-style: none; }
  .contacts li {
    display: flex; align-items: center; gap: 8px;
    font-size: 11.5px; font-weight: 500; line-height: 24px;
  }
  .icon {
    width: 14px; height: 14px; border-radius: 2px;
    background: var(--brand-blue);
    display: flex; align-items: center; justify-content: center;
    flex-shrink: 0;
  }
  .icon svg { width: 10px; height: 10px; fill: var(--paper); }
  .address {
    position: absolute; right: 40px; top: 196px;
    display: flex; gap: 8px; font-size: 12px; font-weight: 500; line-height: 20px;
  }
  .bands { position: absolute; left: 0; bottom: 0; width: 540px; height: 24px; }
</style>
</head>
<body>

  <section class="card card--front" aria-label="Card front">
    <span class="front-name">Maquis Vertex IT</span>
    <span class="front-mark"></span>
  </section>

  <section class="card card--back" aria-label="Card back">
    <div class="holder">
      <p class="holder-name">YOUR NAME</p>
      <p class="holder-title">YOUR TITLE</p>
    </div>

    <div class="brand">
      <span class="brand-name">Maquis Vertex IT</span>
      <span class="brand-mark"></span>
    </div>

    <div class="divider"></div>

    <ul class="contacts">
      <li>
        <span class="icon"><svg viewBox="0 0 10 10"><path d="M2 1l2 0 1 2-1 1c.5 1 1 1.5 2 2l1-1 2 1v2c-4 0-7-3-7-7z"/></svg></span>
        0495718243
      </li>
      <li>
        <span class="icon"></span>
        ateliertech.maquisvertex
      </li>
      <li>
        <span class="icon"><svg viewBox="0 0 10 10"><circle cx="5" cy="5" r="4" fill="none" stroke="#fff" stroke-width="1"/><path d="M1 5h8M5 1c-2 2-2 6 0 8M5 1c2 2 2 6 0 8" fill="none" stroke="#fff" stroke-width=".8"/></svg></span>
        www.maquis-vertex.com
      </li>
      <li>
        <span class="icon"><svg viewBox="0 0 10 10"><path d="M5 1a3 3 0 0 1 3 3c0 2-3 5-3 5S2 6 2 4a3 3 0 0 1 3-3z"/><circle cx="5" cy="4" r="1" fill="#2b87c8"/></svg></span>
        Siret 71384096200018, APE 6203Y
      </li>
    </ul>

    <div class="address">
      <span class="icon"><svg viewBox="0 0 10 10"><path d="M5 1a3 3 0 0 1 3 3c0 2-3 5-3 5S2 6 2 4a3 3 0 0 1 3-3z"/><circle cx="5" cy="4" r="1" fill="#2b87c8"/></svg></span>
      <p>Pierre Blanche<br>Commercial Center<br>20480 Lorvanu</p>
    </div>

    <svg class="bands" viewBox="0 0 540 24" preserveAspectRatio="none" aria-hidden="true">
      <polygon points="0,6 300,6 284,24 0,24" fill="var(--brand-blue)"/>
      <polygon points="300,12 540,12 540,24 290,24" fill="var(--band-grey)"/>
    </svg>
  </section>

</body>
</html>
```